Four Key Ledger Blueprint Presentation

I would like a flyer to hand out to participants at the speeches that we give. We are a CPA firm that specializes in entrepreneurs and realtors. We would like a flyer that looks crisp and clean, that integrates our logo and our company colors (shades of blue & gold). We would like the wording to be as laid out in the attached documents, but design is up to you. We would like a picture to go along with each point and are open to ideas. The flyer should be one page, preferably just the front.

Colors
3176b5
fee18a

Requirements
Must have
• Our logo and the wording supplied.
• A picture to go along with each topic.
Nice to have
• Images that pop, clean look, professional.
Should not have
• Look messy.

```html
<!DOCTYPE html>
<html lang="en">
<head>
<meta charset="utf-8">
<title>Four Key Ledger Blueprint Presentation</title>
<link href="https://fonts.googleapis.com/css2?family=Inter:wght@300;400;500;600;700;800&display=swap" rel="stylesheet">
<style>
  :root {
    --navy: #0f2c4a;
    --navy-deep: #0b2440;
    --gold: #cdb083;
    --gold-soft: #d8bf93;
    --ink: #10263f;
    --paper: #f4f5f8;
    --white: #ffffff;
  }
  * { margin: 0; padding: 0; box-sizing: border-box; }
  html, body { width: 848px; height: 1200px; overflow: hidden; }
  body { font-family: "Inter", Arial, sans-serif; background: var(--paper); color: var(--ink); }
  .flyer { position: relative; width: 848px; height: 1200px; overflow: hidden; background: var(--paper); }

  /* Hero */
  .hero { position: absolute; left: 0; top: 0; width: 848px; height: 440px;
    background: linear-gradient(100deg, #6f8193 0%, #a9b4bf 35%, #c7cdd3 55%, #9fb0bf 100%); overflow: hidden; }
  .hero-band { position: absolute; left: 0; top: 0; }
  .hero-photo { position: absolute; right: 0; top: 0; width: 300px; height: 440px;
    background: radial-gradient(ellipse at 55% 30%, #e7c9a8 0%, #c9a57f 18%, #2a3a55 48%, #1b2a44 80%); opacity: .92; }
  .brand { position: absolute; left: 0; top: 30px; width: 295px; height: 94px; background: var(--white);
    padding: 20px 0 0 38px; }
  .brand-name { display: flex; align-items: center; gap: 8px; font-size: 22px; font-weight: 800; color: var(--navy); letter-spacing: .2px; }
  .brand-mark { width: 12px; height: 12px; background: var(--gold); }
  .brand-tag { margin-top: 10px; font-size: 9.5px; color: var(--ink); font-weight: 500; }

  .title { position: absolute; left: 303px; top: 118px; color: var(--gold-soft); line-height: 1; }
  .title-top { font-size: 34px; font-weight: 300; }
  .title-main { font-size: 78px; font-weight: 700; letter-spacing: -2px; margin-top: 6px; }
  .title-bottom { font-size: 34px; font-weight: 300; margin-top: 6px; padding-left: 92px; }

  /* Agenda */
  .agenda-heading { position: absolute; left: 0; width: 848px; top: 464px; text-align: center;
    font-size: 34px; font-weight: 500; color: var(--navy); letter-spacing: -.3px; }
  .agenda-heading span { color: var(--gold); }
  .point { position: absolute; display: flex; gap: 16px; width: 360px; }
  .point-icon { flex: 0 0 58px; width: 58px; height: 58px; border: 2px solid var(--gold); border-radius: 50%;
    display: flex; align-items: center; justify-content: center; }
  .point-icon svg { width: 30px; height: 30px; stroke: var(--navy); fill: none; stroke-width: 1.4; stroke-linecap: round; stroke-linejoin: round; }
  .point-text { font-size: 11.2px; line-height: 13.8px; font-weight: 500; color: var(--ink); padding-top: 2px; }
  .point-text em { font-style: normal; color: var(--gold); }
  .quote { position: absolute; left: 446px; top: 918px; width: 350px; font-size: 18px; line-height: 22px;
    color: var(--gold); font-weight: 400; }

  /* Footer */
  .footer { position: absolute; left: 0; top: 1061px; width: 848px; height: 139px; background: var(--navy-deep); color: var(--white); }
  .footer-name { position: absolute; left: 71px; top: 18px; font-size: 18px; font-weight: 800; color: var(--gold); letter-spacing: .5px; }
  .footer-tag { position: absolute; left: 71px; top: 42px; font-size: 17px; font-weight: 300; }
  .footer-address { position: absolute; left: 71px; top: 87px; font-size: 12.5px; line-height: 17px; font-weight: 500; }
  .contact { position: absolute; left: 535px; list-style: none; top: 20px; }
  .contact li { display: flex; gap: 20px; font-size: 12.5px; line-height: 16px; font-weight: 500; margin-bottom: 14px; }
  .contact svg { width: 18px; height: 16px; flex: 0 0 18px; fill: #c7ccd3; }
</style>
</head>
<body>
<main class="flyer">
  <header class="hero">
    <svg class="hero-band" width="848" height="440" viewBox="0 0 848 440" aria-hidden="true">
      <polygon points="295,30 558,30 558,110 440,420 345,420 450,124 295,124" fill="#0f2c4a"/>
    </svg>
    <div class="hero-photo" role="img" aria-label="Smiling accountant in a dark blazer holding a tablet"></div>
    <div class="brand">
      <div class="brand-name"><span class="brand-mark"></span>Steadfast Figures</div>
      <div class="brand-tag">A Professional Accounting Corporation</div>
    </div>
    <h1 class="title">
      <div class="title-top">four key</div>
      <div class="title-main">LEDGER</div>
      <div class="title-bottom">blueprint</div>
    </h1>
  </header>

  <h2 class="agenda-heading">Presentation <span>Agenda</span></h2>

  <section class="point" style="left:70px;top:532px;">
    <div class="point-icon"><svg viewBox="0 0 30 30"><path d="M15 3 L25 7 V15 C25 21 20 25 15 27 C10 25 5 21 5 15 V7 Z"/><circle cx="15" cy="15" r="6"/><path d="M17 12.5 C16 11.5 13 11.5 13 13.5 C13 15.5 17 14.5 17 16.5 C17 18.5 14 18.5 13 17.5 M15 10.5 V19.5"/></svg></div>
    <p class="point-text">We will first show you how to eliminate much of your self-employment tax on your return by <em>converting your business into an S Corporation</em>.<br>A business owner making over $120,000 per year can save about $12,000 per year by doing this.</p>
  </section>

  <section class="point" style="left:460px;top:532px;">
    <div class="point-icon"><svg viewBox="0 0 30 30"><circle cx="15" cy="10" r="5"/><path d="M6 26 C6 19 10 17 15 17 C20 17 24 19 24 26"/></svg></div>
    <p class="point-text">We will show you how to <em>hire your children</em> and get $7,500 per child tax free.<br>This will save you $3,000 per child in income tax reduction.</p>
  </section>

  <section class="point" style="left:70px;top:660px;">
    <div class="point-icon"><svg viewBox="0 0 30 30"><path d="M4 13 L15 5 L26 13 M7 12 V25 H23 V12 M12 25 V17 H18 V25 M4 25 H26"/></svg></div>
    <p class="point-text">We will show you how to get tax free income from your corporation by <em>renting your home</em> to the corporation for the board meetings. Many of our clients are getting up to $21,000 in tax free income which could put $8,400 cash into your pocket.</p>
  </section>

  <section class="point" style="left:460px;top:660px;">
    <div class="point-icon"><svg viewBox="0 0 30 30"><path d="M3 11 L15 6 L27 11 L15 16 Z M8 13.5 V20 C8 22 12 23.5 15 23.5 C18 23.5 22 22 22 20 V13.5 M25 12 V19"/></svg></div>
    <p class="point-text">We will discuss how to <em>make your child's college education tax deductible</em>.<br>With college cost spiraling out of control this is a biggie. Most of our clients have a savings of about $12,000 per year of college.</p>
  </section>

  <section class="point" style="left:70px;top:804px;">
    <div class="point-icon"><svg viewBox="0 0 30 30"><path d="M8 4 H19 L23 8 V26 H8 Z M19 4 V8 H23 M11 12 H20 M11 16 H20 M11 20 H17"/></svg></div>
    <p class="point-text">We will show you the <em>easiest way to track your expenses</em> so that the only thing you will have to do to have rock solid books is to take a picture of the receipt and throw it away.<br>It doesn't get any better than that.</p>
  </section>

  <section class="point" style="left:460px;top:804px;">
    <div class="point-icon"><svg viewBox="0 0 30 30"><path d="M9 4 H21 V11 C21 15 18 17 15 17 C12 17 9 15 9 11 Z M9 6 H5 C5 10 7 12 9 12 M21 6 H25 C25 10 23 12 21 12 M15 17 V22 M10 26 H20 L19 22 H11 Z"/></svg></div>
    <p class="point-text">Our <em>grand finale</em> is to show you how to use, not one, but two corporations to get a several hundred thousand dollar tax deferral, get an interest free loan from the government and use that money to grow your business and your wealth.</p>
  </section>

  <section class="point" style="left:70px;top:922px;">
    <div class="point-icon"><svg viewBox="0 0 30 30"><rect x="5" y="7" width="20" height="18" rx="1"/><path d="M5 12 H25 M10 4 V9 M20 4 V9 M10 17 L13.5 20.5 L20 15"/></svg></div>
    <p class="point-text">Next, we show you the importance of tax planning and why it is critical to <em>meet with your CPA</em> before the end of the year and not just when you do your tax preparation.</p>
  </section>

  <blockquote class="quote">“If they drive by with a machine gun you don’t have to stand up”</blockquote>

  <footer class="footer">
    <div class="footer-name">STEADFAST FIGURES</div>
    <div class="footer-tag">A Professional Accounting Corporation</div>
    <address class="footer-address" style="font-style:normal;">820 Orchard Ave, Ste. B, Lodi, CA 95240<br>www.steadfastfigurescpas.com</address>
    <ul class="contact">
      <li><svg viewBox="0 0 18 16"><path d="M4 1 L7 4 L5.5 6.5 C6.5 8.5 8.5 10.5 10.5 11.5 L13 10 L16 13 L14 15 C8 15 2 9 2 3 Z"/></svg>209-555-0142</li>
      <li><svg viewBox="0 0 18 16"><path d="M5 1 H13 V5 H5 Z M2 6 H16 V12 H13 V15 H5 V12 H2 Z M6 10 V13 H12 V10 Z"/></svg>209-555-0187</li>
      <li><svg viewBox="0 0 18 16"><path d="M1 3 H17 V14 H1 Z M1 3 L9 9.5 L17 3" stroke="#0b2440" stroke-width="1.2"/></svg><span>Dana@steadfastfigurescpas.com,<br>Marcus@steadfastfigurescpas.com</span></li>
    </ul>
  </footer>
</main>
</body>
</html>
```